Digital Marketing Agency Landing Page

At VELMIK, we offer a comprehensive solution for solar companies' client acquisition needs in the rapidly growing industry. We handle end-to-end client acquisition, meaning we manage the entire lifecycle of capturing new clients—from initial lead generation to delivering the ready-to-buy homeowner. Our expertise in targeted advertising, data analytics, and customer relationship management ensures that we not only find potential customers but also nurture them through tailored engagement strategies until they are ready to make a purchase. By entrusting us with your client acquisition process, solar companies can focus on what they do best—providing sustainable energy solutions—while we work behind the scenes to grow your customer base and increase your market share.

We need to restructure our website to make it more professional. We don't need any complex functionalities. We are looking for someone that is good in design and can build a visually aesthetic website following our brand image. We only need a landing page and a lead form in the end. I would like to have only one page, but a relatively big one where people scroll down. I would like to have a minimal and classy look. Something that is timeless and elegant.

Structure:

initial page
About us
How we operate
Get in touch

Target Market(s)

Solar Comapanies

Industry/Entity Type

Marketing solautions

Coding

Coded - Design and coding required

Number of Pages Required

1 page

Requirements
Nice to have
• Inspirations: https://www.qz.lo/ https://www.tobinwell.com/ https://www.mendocrate.com/ https://pravo.com/

```html
<!DOCTYPE html>
<html lang="en">
<head>
<meta charset="utf-8">
<title>VELMIK — Client Acquisition for Solar Companies</title>
<link href="https://fonts.googleapis.com/css2?family=Montserrat:wght@300;400;500;600;700&display=swap" rel="stylesheet">
<style>
  :root{
    --navy:#0f222d;
    --sand:#ebe7d9;
    --mist:#ebeae5;
    --backdrop:#e0ddcc;
    --ink:#0f222d;
    --muted:#4d5860;
    --rule:#9aa2a2;
    --photo-a:#8e9493;
    --photo-b:#c9cbc6;
  }
  *{margin:0;padding:0;box-sizing:border-box}
  html,body{width:1200px;height:3335px;overflow:hidden}
  body{background:var(--backdrop);font-family:"Montserrat",sans-serif;color:var(--ink);position:relative}
  .abs{position:absolute}

  /* style guide header */
  .guide-logo{left:203px;top:133px;font-size:27px;font-weight:300;letter-spacing:1px;color:var(--ink)}
  .guide-title{font-size:25px;font-weight:400;color:var(--ink)}
  .guide-sub{font-size:15px;font-weight:300;color:var(--muted)}
  .swatch{width:42px;height:42px;border-radius:50%}
  .swatch-code{font-size:10px;color:var(--muted);width:60px;text-align:center}

  /* page */
  .page{left:223px;top:280px;width:791px;height:2952px;background:var(--sand);overflow:hidden}
  .nav{left:0;top:0;width:791px;height:47px;background:var(--mist)}
  .brand{left:74px;top:15px;font-size:14px;font-weight:400;letter-spacing:.5px;color:var(--ink)}
  .nav-link{top:18px;font-size:7.5px;font-weight:400}
  .nav-rule{left:475px;top:23px;width:48px;height:1px;background:var(--ink)}
  .nav-contact{left:603px;top:18px;font-size:7.5px;font-weight:400}

  .hero{left:0;top:47px;width:791px;height:384px;background:var(--navy)}
  .hero-lines{left:440px;top:0;width:351px;height:384px;background:linear-gradient(135deg,rgba(255,255,255,.05),rgba(255,255,255,0) 70%)}
  .side-label{left:74px;writing-mode:vertical-rl;transform:rotate(180deg);font-size:7px;letter-spacing:.5px;color:var(--muted);text-transform:uppercase}
  .hero .side-label{color:#9aa5ab;top:98px}
  .hero-title{left:198px;top:96px;width:560px;font-size:34px;line-height:40px;font-weight:400;color:#fff;white-space:nowrap}
  .hero-title strong{font-weight:700;color:var(--sand)}
  .btn-outline{left:198px;top:236px;width:110px;height:30px;border:1px solid #fff;color:#fff;font-size:7.5px;font-weight:600;display:flex;align-items:center;justify-content:center;gap:6px}

  .stat-num{font-size:22px;font-weight:400}
  .stat-text{font-size:7.5px;line-height:13px;color:var(--muted);white-space:nowrap}

  .photo{background:linear-gradient(160deg,var(--photo-b),var(--photo-a))}
  .corner-tile{left:0;top:985px;width:74px;height:74px;background:var(--navy)}

  .section-title{left:198px;font-size:21px;line-height:26px;font-weight:400;white-space:nowrap}
  .body-copy{font-size:8px;line-height:13.3px;color:var(--muted)}
  .body-copy p+p{margin-top:13px}
  .divider{left:0;width:791px;height:1px;background:var(--rule)}
  .operate{left:0;top:1636px;width:791px;height:825px;background:var(--mist)}

  .contact-panel{left:74px;top:2616px;width:717px;height:336px;background:var(--navy);color:#fff}
  .contact-intro{left:124px;top:51px;width:200px;font-size:12px;line-height:17.5px;font-weight:400}
  .contact-rule{left:124px;width:180px;height:1px;background:#7d8a90}
  .contact-line{left:124px;top:150px;font-size:9px}
  .field{left:410px;width:233px;height:26px;border-bottom:1px solid #56646b;font-size:7.5px;color:#dfe3e3;padding-top:10px}
  .btn-solid{left:410px;top:250px;width:123px;height:27px;background:var(--sand);color:var(--ink);font-size:7.5px;font-weight:600;display:flex;align-items:center;justify-content:center;gap:6px}
</style>
</head>
<body>

<header>
  <div class="abs guide-logo">VELMIK</div>
  <div class="abs guide-title" style="left:569px;top:102px">Fonts:</div>
  <div class="abs guide-sub" style="left:569px;top:149px">Montserrat</div>
  <div class="abs guide-title" style="left:890px;top:102px">Colors:</div>
  <div class="abs swatch" style="left:890px;top:137px;background:var(--navy)"></div>
  <div class="abs swatch" style="left:941px;top:137px;background:var(--sand)"></div>
  <div class="abs swatch" style="left:993px;top:137px;background:var(--mist)"></div>
  <div class="abs swatch-code" style="left:881px;top:187px">#0f222d</div>
  <div class="abs swatch-code" style="left:932px;top:187px">#ebe7d9</div>
  <div class="abs swatch-code" style="left:984px;top:187px">#ebeae5</div>
</header>

<main class="abs page">
  <nav class="abs nav">
    <div class="abs brand">VELMIK</div>
    <span class="abs nav-link" style="left:198px">About</span>
    <span class="abs nav-link" style="left:256px">How We Operate</span>
    <span class="abs nav-link" style="left:352px">Get in Touch</span>
    <span class="abs nav-rule"></span>
    <span class="abs nav-contact">+1 555 014 2290 &nbsp;|&nbsp; info@velmik.com</span>
  </nav>

  <section class="abs hero">
    <div class="abs hero-lines" role="img" aria-label="Faint diagonal line texture"></div>
    <span class="abs side-label">Welcome to Velmik</span>
    <h1 class="abs hero-title"><strong>Bridging the Gap</strong> between<br>the Solar Experts and<br>Value-Driven Homeowners</h1>
    <a class="abs btn-outline">How We Operate
      <svg width="9" height="6" viewBox="0 0 9 6"><path d="M0 3h8M6 1l2 2-2 2" stroke="#fff" fill="none" stroke-width=".8"/></svg></a>
  </section>

  <section class="stats">
    <span class="abs side-label" style="top:462px">Intro</span>
    <div class="abs" style="left:292px;top:465px">
      <div class="stat-num">500+</div>
      <p class="stat-text" style="margin-top:3px">VELMIK has successfully served over 500 solar<br>companies with its comprehensive solutions.</p>
    </div>
    <div class="abs" style="left:539px;top:465px">
      <div class="stat-num">150</div>
      <p class="stat-text" style="margin-top:3px">Their expertise have contributed to the<br>successful launch of 150 new solar ventures.</p>
    </div>
    <div class="abs" style="left:292px;top:557px">
      <div class="stat-num">246</div>
      <p class="stat-text" style="margin-top:3px">Comprehensive solutions to 246 companies,<br>helping them enhance their performance</p>
    </div>
    <div class="abs" style="left:539px;top:557px">
      <div class="stat-num">37%</div>
      <p class="stat-text" style="margin-top:3px">VELMIK's expertise has led to a 37% increase<br>in efficiency for numerous solar projects</p>
    </div>
  </section>

  <div class="abs photo" style="left:74px;top:663px;width:717px;height:396px" role="img" aria-label="Photo of two engineers in hard hats walking between rows of solar panels"></div>
  <div class="abs corner-tile"></div>

  <section class="about">
    <span class="abs side-label" style="top:1119px">About</span>
    <h2 class="abs section-title" style="top:1114px">At VELMIK, we offer a<br>comprehensive solution<br>for solar companies' client<br>acquisition needs in the<br>rapidly growing industry.</h2>
    <div class="abs body-copy" style="left:551px;top:1114px;width:170px">
      <p>Our expertise in targeted advertising, and customer relationship management ensures that we not only find potential customers but also nurture them through tailored engagement strategies until they are ready to make a purchase.</p>
      <p>By entrusting us with client acquisition process, solar companies can focus on what they do best—providing sustainable energy solutions—while we work behind the scenes to grow your customer base and increase your market share.</p>
    </div>
    <div class="abs photo" style="left:198px;top:1331px;width:519px;height:246px" role="img" aria-label="Photo of wind turbines rising behind a field of solar panels"></div>
  </section>

  <div class="abs divider" style="top:1636px"></div>

  <section class="abs operate">
    <span class="abs side-label" style="top:59px">How we operate</span>
    <h2 class="abs section-title" style="top:56px">Providing sustainable<br>energy solutions while we<br>work behind the scenes<br>to grow your customer<br>base and increase your<br>market share</h2>
    <div class="abs body-copy" style="left:551px;top:56px;width:170px">
      <p>By entrusting us with client acquisition process, solar companies can focus on what they do best—providing sustainable energy solutions—while we work behind the scenes to grow your customer base and increase your market share.</p>
    </div>
    <div class="abs photo" style="left:198px;top:253px;width:519px;height:198px" role="img" aria-label="Photo of a specialist reviewing a tablet between solar panels"></div>
    <div class="abs photo" style="left:198px;top:470px;width:344px;height:149px" role="img" aria-label="Photo of hands working over a model with a small wind turbine and solar panel"></div>
    <div class="abs photo" style="left:563px;top:470px;width:136px;height:214px" role="img" aria-label="Photo of a smiling team member holding a tablet"></div>
    <div class="abs body-copy" style="left:198px;top:680px;width:345px;font-size:7.5px;line-height:13px">
      <p>By partnering with our marketing expertise, solar companies can dedicate their energy to advancing sustainable solutions, leaving the customer acquisition process to us.</p>
      <p style="margin-top:7px">Furthermore, our commitment to your success extends beyond just increasing your customer base. We strive to enhance your market share by staying ahead of industry trends, adjusting our strategies to the ever-evolving solar landscape, and ensuring that your brand remains at the forefront of sustainable energy innovation.</p>
    </div>
  </section>

  <div class="abs divider" style="top:2461px"></div>

  <section class="contact">
    <span class="abs side-label" style="top:2522px">Contact us</span>
    <h2 class="abs section-title" style="top:2517px">Have a project in mind?<br>Let’s get in touch</h2>
    <div class="abs contact-panel">
      <p class="abs contact-intro">Let’s work together. You can either fill the inquiry form or contact us via phone</p>
      <div class="abs contact-rule" style="top:127px"></div>
      <div class="abs contact-line">info@velmik.com &nbsp;-&nbsp; + (0) 1 555 014 2290</div>
      <div class="abs contact-rule" style="top:187px"></div>
      <form>
        <div class="abs field" style="top:50px">Company name</div>
        <div class="abs field" style="top:88px">Phone Number</div>
        <div class="abs field" style="top:125px">Email Address</div>
        <div class="abs field" style="top:163px">City</div>
        <div class="abs field" style="top:199px">Inquiry</div>
        <a class="abs btn-solid">Submit Your Inquiry
          <svg width="9" height="6" viewBox="0 0 9 6"><path d="M0 3h8M6 1l2 2-2 2" stroke="#0f222d" fill="none" stroke-width=".8"/></svg></a>
      </form>
    </div>
  </section>
</main>

</body>
</html>
```